「アオバリンク」をぜひ利用してみたいと思わせる構成をお願いいたします。企業採用活動に関して信頼を置いて相談ができることを意識させるイメージでデザインを希望いたします。
イメージキーワード : 爽やか、現代的、おしゃれ

構成、文章に関しましては添付のラフ案をご参照ください。
一枚物のLPでフォームが表示されるイメージです。

※スマホ版・PC版双方のデザインをお願いいたします。

参考デザインとしてURLを記載いたします。
レイアウトベースイメージはこちら「ひらけの仕事」
https://hirake-shigoto.com/html/pr/ad/pc/basic/3040/009/

デザインイメージはこちら「東陽コルディア」
https://www.kordia-toyo.jp/recruit/

※ひらけの仕事のレイアウトをベースに色味、写真・イラストの雰囲気は「東陽コルディア」のイメージです。

納品データはaiデータでお願いいたします。
1枚もののページでPC版の幅は1000px、スマホ版の幅は750pxで製作予定です。

素材に関しましてはゆるえ素材庫・フォトノハラのアカウントを保有しておりますのでそちらのカンプデータをなるべくご使用いただけましたら幸いです。
※イメージに合う物がない場合、別素材でもかまいません。
https://k-sparrow.com/

素晴らしいデザインで、当方のイメージ合わせご制作いただきありがとうございました。

皆様、この度は弊社のLPのデザインコンペに多数ご応募いただきましてありがとうございました。
また、コンペでの発注をさせていただくことがありました際は、何卒よろしくお願い申し上げます。

```html
<!DOCTYPE html>
<html lang="ja">
<head>
<meta charset="utf-8">
<title>アオバリンク | 30代〜40代ミドル層 管理者採用支援サービス</title>
<link rel="stylesheet" href="https://fonts.googleapis.com/css2?family=Noto+Sans+JP:wght@400;500;700;900&family=Dancing+Script:wght@500;700&display=swap">
<style>
:root{
  --teal:#2ba6a3;
  --teal-dark:#1f8a89;
  --teal-pale:#e8f4f4;
  --navy:#1e3647;
  --navy-deep:#18303f;
  --orange:#f29a1f;
  --ink:#3a4650;
  --muted:#6f7b84;
  --line:#c9d3d8;
  --white:#ffffff;
  --bg:#f5f8f9;
}
*{margin:0;padding:0;box-sizing:border-box}
html,body{width:1200px;height:3060px;overflow:hidden}
body{font-family:"Noto Sans JP",sans-serif;color:var(--ink);background:var(--white);position:relative}
.section{position:absolute;left:0;width:1200px;overflow:hidden}
.script{font-family:"Dancing Script",cursive;font-weight:700;color:var(--teal);line-height:1.2;white-space:nowrap}

/* hero */
.hero{top:0;height:400px}
.hero-photo{position:absolute;inset:0;background:linear-gradient(110deg,#2f8f93 0%,#3fa5a5 45%,#7fc3c2 75%,#b9dedd 100%)}
.hero-copy{position:absolute;left:120px;top:110px;color:var(--white)}
.hero-lead{font-size:22px;font-weight:700;letter-spacing:.08em}
.hero-title{font-size:44px;font-weight:900;line-height:1.35;letter-spacing:.04em;margin-top:6px}
.hero-brand{display:inline-block;margin-top:18px;background:var(--teal);border:2px solid var(--white);color:var(--white);font-size:22px;font-weight:700;padding:6px 22px;letter-spacing:.1em}
.hero-tags{display:flex;gap:12px;margin-top:22px}
.hero-tags span{background:rgba(255,255,255,.9);color:var(--teal-dark);font-size:15px;font-weight:700;padding:6px 14px}
.form-card{position:absolute;left:808px;top:18px;width:338px;background:var(--white);padding:18px 22px 20px;box-shadow:0 4px 14px rgba(0,0,0,.15)}
.form-head{display:flex;align-items:center;justify-content:center;gap:14px;color:var(--navy)}
.form-head .brand{font-size:16px;font-weight:700;line-height:1.1;text-align:left}
.form-head .brand strong{display:block;font-size:26px;font-weight:900;color:var(--navy)}
.free{width:48px;height:48px;border-radius:50%;background:var(--orange);color:var(--white);font-size:14px;font-weight:700;display:flex;align-items:center;justify-content:center}
.field{height:34px;border:1px solid var(--line);margin-top:10px;font-size:13px;color:#9aa5ad;padding:0 10px;display:flex;align-items:center}
.form-card .field:first-of-type{margin-top:14px}
.btn{display:flex;align-items:center;justify-content:center;gap:10px;background:var(--orange);color:var(--white);font-weight:700;border-radius:30px}
.btn::after{content:"";width:8px;height:8px;border-top:2px solid var(--white);border-right:2px solid var(--white);transform:rotate(45deg)}
.form-card .btn{height:42px;font-size:14px;margin-top:16px}
.form-note{position:absolute;left:808px;top:262px;width:338px;background:var(--white);font-size:13px;line-height:1.7;padding:12px 18px;color:var(--ink)}

/* problem */
.problem{top:400px;height:560px;background:var(--bg)}
.problem .script{position:absolute;left:60px;top:30px;font-size:80px}
.problem-q{position:absolute;left:0;width:1200px;top:56px;text-align:center;font-size:24px;font-weight:700;color:var(--navy)}
.band-title{position:absolute;left:250px;width:850px;top:110px;display:flex;align-items:center;gap:20px;font-size:22px;font-weight:700;color:var(--navy)}
.band-title::before,.band-title::after{content:"";flex:1;height:2px;background:var(--navy)}
.worries{position:absolute;left:110px;top:170px;display:flex;gap:20px}
.worry{width:306px;height:200px;background:var(--white);box-shadow:0 2px 8px rgba(0,0,0,.08)}
.worry h3{background:var(--navy);color:var(--white);font-size:20px;font-weight:700;text-align:center;padding:14px 0}
.worry p{font-size:15px;line-height:1.8;text-align:center;padding:20px 24px 0}
.arrow-down{position:absolute;left:0;top:450px;width:1200px;height:110px}

/* solution */
.solution{top:960px;height:700px;background:var(--white)}
.solution-band{position:absolute;left:340px;top:50px;width:520px;height:64px;background:var(--teal);color:var(--white);font-size:28px;font-weight:700;display:flex;align-items:center;padding-left:40px;z-index:1}
.solution .script{position:absolute;left:850px;top:14px;font-size:90px;z-index:2}
.solution-text{position:absolute;left:120px;top:190px;width:470px;font-size:15px;line-height:2}
.solution-illust{position:absolute;left:620px;top:170px;width:480px;height:330px;background:linear-gradient(160deg,#eef6f6,#cfe6e6)}
.solution .btn{position:absolute;left:450px;top:580px;width:300px;height:50px;font-size:15px}

/* reason */
.reason{top:1660px;height:590px;background:var(--white)}
.reason .script{position:absolute;left:0;width:1200px;text-align:center;top:14px;font-size:80px}
.reason-sub{position:absolute;left:100px;width:1000px;top:115px;display:flex;align-items:center;gap:20px;font-size:22px;font-weight:700;color:var(--navy)}
.reason-sub::before,.reason-sub::after{content:"";flex:1;height:2px;background:var(--navy)}
.reasons{position:absolute;left:110px;top:175px;display:flex;gap:20px}
.reason-card{width:306px;height:270px;background:var(--white);box-shadow:0 2px 10px rgba(0,0,0,.12);padding:24px 24px 0}
.reason-card .icon{width:64px;height:64px;margin:0 auto;display:block}
.reason-card h3{font-size:18px;font-weight:700;color:var(--navy);text-align:center;margin-top:14px;padding-bottom:10px;border-bottom:2px solid var(--teal)}
.reason-card p{font-size:14px;line-height:1.8;margin-top:12px}
.reason .btn{position:absolute;left:450px;top:500px;width:300px;height:50px;font-size:15px}

/* precedent */
.precedent{top:2250px;height:730px}
.precedent-bg{position:absolute;inset:0;background:linear-gradient(180deg,#3aa9a7 0%,#2b9897 55%,#227f80 100%)}
.precedent .script{position:absolute;left:60px;top:12px;font-size:88px;color:var(--white)}
.precedent-sub{position:absolute;left:440px;width:660px;top:115px;display:flex;align-items:center;gap:20px;font-size:22px;font-weight:700;color:var(--white)}
.precedent-sub::before,.precedent-sub::after{content:"";flex:1;height:2px;background:var(--white)}
.cases{position:absolute;left:110px;top:190px;display:flex;gap:20px}
.case{position:relative;width:306px;height:340px;background:var(--white);padding:40px 22px 0}
.case .tag{position:absolute;left:0;top:-14px;background:var(--navy);color:var(--white);font-size:15px;font-weight:700;padding:4px 16px}
.case h3{font-size:17px;font-weight:700;color:var(--teal-dark);line-height:1.5;text-align:center;border-top:2px solid var(--teal);border-bottom:2px solid var(--teal);padding:8px 0;min-height:76px;display:flex;align-items:center;justify-content:center}
.case p{font-size:14px;line-height:1.8;margin-top:16px}
.precedent-note{position:absolute;left:0;width:1200px;top:580px;text-align:center;color:var(--white);font-size:16px}
.precedent .btn{position:absolute;left:450px;top:630px;width:300px;height:50px;font-size:15px}

/* footer */
.footer{top:2980px;height:80px;background:var(--navy-deep);color:var(--white);font-size:15px;display:flex;align-items:center;justify-content:center}
</style>
</head>
<body>

<header class="section hero">
  <div class="hero-photo" role="img" aria-label="オフィスで打ち合わせをするビジネスパーソンの写真（ティール色のオーバーレイ）"></div>
  <div class="hero-copy">
    <p class="hero-lead">会社の将来を任せる</p>
    <h1 class="hero-title">30代〜40代ミドル層<br>管理者採用支援サービス</h1>
    <p class="hero-brand">アオバリンク</p>
    <div class="hero-tags"><span>管理職・幹部候補</span><span>年収800万</span><span>職業人材</span></div>
  </div>
  <form class="form-card">
    <div class="form-head">
      <p class="brand">アオバリンク<strong>資料ダウンロード</strong></p>
      <span class="free">無料</span>
    </div>
    <div class="field">会社名</div>
    <div class="field">お名前</div>
    <div class="field">メールアドレス</div>
    <div class="btn">無料で資料をダウンロードする</div>
  </form>
  <p class="form-note">この資料は、管理職採用でお悩みの企業様へ向けてサービスの概要と導入の流れをまとめたものです。お気軽にダウンロードください。</p>
</header>

<section class="section problem">
  <p class="script">Problem</p>
  <h2 class="problem-q">こんな経験ありませんか?</h2>
  <p class="band-title">管理職採用における3つの悩み</p>
  <div class="worries">
    <div class="worry"><h3>新規事業への挑戦</h3><p>新たな事業にチャレンジしたいが任せられる人材がいない</p></div>
    <div class="worry"><h3>DX進化</h3><p>DX推進を担えるITの知見を持った管理職が見つからない</p></div>
    <div class="worry"><h3>社内公募・抜擢</h3><p>管理職になりたいと思う人材がなかなか育たない</p></div>
  </div>
  <svg class="arrow-down" viewBox="0 0 1200 110" aria-hidden="true"><polygon points="440,0 760,0 760,30 600,110 440,30" fill="#1e3647"/></svg>
</section>

<section class="section solution">
  <p class="solution-band">管理職不足を解決します。</p>
  <p class="script">Solution</p>
  <p class="solution-text">近年の採用市場では、ミドル層の管理職人材の獲得競争が激しくなっています。DXの推進や新規事業の立ち上げなど、企業に求められる変化のスピードは年々速くなり、それを担うリーダーの存在が欠かせません。しかし多くの企業では、社内での育成が追いつかず、外部からの採用にも苦戦しています。アオバリンクは、30代〜40代の即戦力人材に特化した採用支援で、貴社の課題に合った人材をご紹介します。まずはお気軽にご相談ください。</p>
  <div class="solution-illust" role="img" aria-label="チームで働くビジネスパーソンのイラスト"></div>
  <div class="btn">無料で資料をダウンロードする</div>
</section>

<section class="section reason">
  <p class="script">Reason</p>
  <p class="reason-sub">アオバリンクが選ばれる3つの理由</p>
  <div class="reasons">
    <div class="reason-card">
      <svg class="icon" viewBox="0 0 64 64" aria-hidden="true"><rect x="10" y="8" width="44" height="50" rx="4" fill="none" stroke="#2ba6a3" stroke-width="4"/><path d="M20 28l8 8 16-16" fill="none" stroke="#2ba6a3" stroke-width="4"/></svg>
      <h3>手間が省ける</h3>
      <p>求人作成から応募者対応まで専任担当がサポートするため、採用担当者の手間を大きく減らせます。</p>
    </div>
    <div class="reason-card">
      <svg class="icon" viewBox="0 0 64 64" aria-hidden="true"><circle cx="24" cy="22" r="9" fill="none" stroke="#2ba6a3" stroke-width="4"/><circle cx="44" cy="26" r="7" fill="none" stroke="#2ba6a3" stroke-width="4"/><path d="M8 54c2-12 10-18 16-18s14 6 16 18M38 54c2-9 6-14 12-14" fill="none" stroke="#2ba6a3" stroke-width="4"/></svg>
      <h3>エンゲージメント低下解消</h3>
      <p>入社後の定着まで見据えたマッチングで、組織のエンゲージメント低下を防ぎます。</p>
    </div>
    <div class="reason-card">
      <svg class="icon" viewBox="0 0 64 64" aria-hidden="true"><circle cx="32" cy="32" r="22" fill="none" stroke="#2ba6a3" stroke-width="4"/><circle cx="32" cy="32" r="12" fill="none" stroke="#2ba6a3" stroke-width="4"/><circle cx="32" cy="32" r="4" fill="#2ba6a3"/></svg>
      <h3>ピンポイント採用が可能</h3>
      <p>業界や職種、プロジェクトの経験など、求める条件に合った人材をピンポイントでご紹介します。</p>
    </div>
  </div>
  <div class="btn">無料で資料をダウンロードする</div>
</section>

<section class="section precedent">
  <div class="precedent-bg" role="img" aria-label="オフィスの風景写真（ティール色のオーバーレイ）"></div>
  <p class="script">Precedent</p>
  <p class="precedent-sub">会社アオバリンク成功事例</p>
  <div class="cases">
    <div class="case"><span class="tag">A社</span><h3>【東京本社上場】<br>デジタルマーケティング責任者</h3><p>事業拡大に伴いデジタル施策を統括できる人材を募集。広告運用とチーム育成の経験を持つ40代の方が入社し、半年で成果を上げています。</p></div>
    <div class="case"><span class="tag">B社</span><h3>営業企画ディレクター</h3><p>営業戦略の立案から実行まで担える人材を募集。同業界で管理職経験のある30代後半の方が入社し、新たな営業体制づくりを推進中です。</p></div>
    <div class="case"><span class="tag">C社</span><h3>【新規立ち上げ】<br>ネット系のサービス責任者</h3><p>新規サービスの立ち上げを任せられる責任者を募集。事業開発の経験を持つ方が入社し、リリースまでを牽引しています。</p></div>
  </div>
  <p class="precedent-note">これは、一例です。その他にも様々な成功事例があります。</p>
  <div class="btn">無料で資料をダウンロードする</div>
</section>

<footer class="section footer">Copyright (C) 2014-2021 KITA SPARROW. All Rights Reserved.</footer>

</body>
</html>
```